Kestrelway Advisory logo/business card design -- a digital consulting company

I've just restarted a consulting company I had years ago--Kestrelway Advisory. Now I need a new business card and updated logo. The original logo was simple enough: a chart-like progression atop a grid (see the attached file). I do strategy work, and the chart is meant to show incremental growth and profit. I'd like the reincarnation of my logo to be 3D, with both the grid and arrow rotated on their axis.

I'll want to use the logo on my website as well. I'm open to color schemes, fonts, etc.

Target Market(s)

Business-to-Business. Target market is corporate.

Industry/Entity Type

Business

Contact Information for Business Card

Logo on one-side; name and other contact info on the back

Font styles to use
Serif
Sans Serif

Requirements
Nice to have
• Kestrelway Advisory refers to the concept of "bootstrapping" or making incremental changes to grow with minimal risk and financial exposure, and self-sufficiency (think of the phrase "to pull oneself by one's bootstraps.")

```html
<!DOCTYPE html>
<html lang="en">
<head>
<meta charset="utf-8">
<title>Kestrelway Advisory – Business Card</title>
<link rel="stylesheet" href="https://fonts.googleapis.com/css2?family=Montserrat:wght@300;400;600;700&display=swap">
<style>
  :root {
    --backdrop: #8a6a44;
    --backdrop-dark: #6e5232;
    --charcoal: #23272d;
    --charcoal-light: #4a4f57;
    --brand-red: #e0202c;
    --brand-red-dark: #b5121d;
    --steel: #8e939a;
    --steel-light: #c9ccd0;
    --white: #ffffff;
  }
  * { box-sizing: border-box; margin: 0; padding: 0; }
  html, body {
    width: 1200px; height: 1023px; overflow: hidden;
    background: radial-gradient(ellipse at center, var(--backdrop) 0%, var(--backdrop-dark) 100%);
    font-family: "Montserrat", Arial, sans-serif;
  }
  .canvas {
    position: relative; width: 1200px; height: 1023px;
  }
  .card {
    position: absolute; left: 250px; width: 700px; height: 400px;
    border-radius: 6px; overflow: hidden;
    box-shadow: 0 14px 30px rgba(0,0,0,0.45);
  }
  .card-front { top: 90px; background: linear-gradient(120deg, var(--charcoal) 0%, var(--charcoal-light) 55%, var(--charcoal) 100%); }
  .card-back  { top: 533px; background: linear-gradient(135deg, var(--brand-red) 0%, var(--brand-red-dark) 100%); }
  .card-art { position: absolute; inset: 0; width: 100%; height: 100%; }

  .brand-lockup {
    position: absolute; left: 70px; top: 150px;
    display: flex; align-items: center; gap: 18px;
  }
  .brand-dot {
    width: 26px; height: 26px; border-radius: 50%; background: var(--brand-red);
  }
  .brand-name {
    color: var(--brand-red); font-weight: 700; font-size: 40px;
    line-height: 1.1; letter-spacing: 2px; text-transform: uppercase;
  }
  .front-web {
    position: absolute; right: 28px; bottom: 26px;
    color: var(--white); font-size: 15px; font-weight: 300; letter-spacing: 0.5px;
  }

  .contact-block { position: absolute; left: 60px; top: 70px; color: var(--white); }
  .person-name { font-size: 34px; font-weight: 700; letter-spacing: 1px; text-transform: uppercase; }
  .person-role { font-size: 18px; font-weight: 300; margin-top: 4px; margin-bottom: 44px; }
  .contact-list { list-style: none; }
  .contact-item {
    display: flex; align-items: center; gap: 14px;
    font-size: 18px; font-weight: 300; margin-bottom: 16px;
  }
  .contact-icon { width: 22px; height: 22px; flex: none; }
</style>
</head>
<body>
<main class="canvas">

  <section class="card card-front" aria-label="Card front">
    <svg class="card-art" viewBox="0 0 700 400" aria-hidden="true">
      <defs>
        <linearGradient id="steelBand" x1="0" y1="0" x2="1" y2="0">
          <stop offset="0" stop-color="#5d6269"/>
          <stop offset="0.5" stop-color="#c9ccd0"/>
          <stop offset="1" stop-color="#8e939a"/>
        </linearGradient>
      </defs>
      <path d="M470 400 C 560 300, 610 150, 640 0 L 700 0 L 700 400 Z" fill="var(--brand-red)"/>
      <path d="M430 400 C 525 300, 575 150, 600 0 L 640 0 C 610 150, 560 300, 470 400 Z" fill="url(#steelBand)"/>
    </svg>
    <div class="brand-lockup">
      <span class="brand-dot"></span>
      <span class="brand-name">Kestrelway<br>Advisory</span>
    </div>
    <p class="front-web">www.kestrelwayadvisory.com</p>
  </section>

  <section class="card card-back" aria-label="Card back">
    <svg class="card-art" viewBox="0 0 700 400" aria-hidden="true">
      <path d="M560 400 C 620 300, 650 150, 665 0 L 700 0 L 700 400 Z" fill="var(--charcoal)"/>
    </svg>
    <div class="contact-block">
      <h1 class="person-name">Dana Marsh</h1>
      <p class="person-role">Director</p>
      <ul class="contact-list">
        <li class="contact-item">
          <svg class="contact-icon" viewBox="0 0 24 24"><path fill="#fff" d="M6.6 10.8a15 15 0 0 0 6.6 6.6l2.2-2.2c.3-.3.7-.4 1-.2 1.1.4 2.3.6 3.6.6.6 0 1 .4 1 1V20c0 .6-.4 1-1 1A17 17 0 0 1 3 4c0-.6.4-1 1-1h3.5c.6 0 1 .4 1 1 0 1.3.2 2.5.6 3.6.1.3 0 .7-.2 1z"/></svg>
          0161 555 0148
        </li>
        <li class="contact-item">
          <svg class="contact-icon" viewBox="0 0 24 24"><rect x="2" y="5" width="20" height="14" rx="2" fill="none" stroke="#fff" stroke-width="2"/><path d="M3 6l9 7 9-7" fill="none" stroke="#fff" stroke-width="2"/></svg>
          dana@kestrelwayadvisory.com
        </li>
        <li class="contact-item">
          <svg class="contact-icon" viewBox="0 0 24 24"><circle cx="12" cy="12" r="9.5" fill="none" stroke="#fff" stroke-width="2"/><path d="M2.5 12h19M12 2.5c3 3 3 16 0 19M12 2.5c-3 3-3 16 0 19" fill="none" stroke="#fff" stroke-width="1.6"/></svg>
          www.kestrelwayadvisory.com
        </li>
      </ul>
    </div>
  </section>

</main>
</body>
</html>
```